uk based ecommerce website requires fresh look ,high quality look and feel

we are a web based company selling eco friendly ground reinforcement grids to diy and construction sectors
our existing website is www.plumbrookpaving.co.uk ,

we have already updated the logo so that is the branding sorted .so we need a ecommerce website that is very much up-to date in design and layout and which has content management system for ease of use so that we can add products and information as required.

Use current logo as reference for colour scheme.
www.plumbrookpaving.co.uk

The current website has 6 pages accessible through the navigation bar, I would now like 5 pages, removing the need for the Trade Enquiries page possibly have it with along with contact us.

Target Market(s)

construction industry , diy end users,
retail market, landscapers, gardeners

Industry/Entity Type

Construction

Font styles to use
Other font styles liked:
• logo font prometo

Colors
f78f20
9bcb3c

Requirements
Must have
• logo colours and logo design in website with cms responsive design for tablet and mobile devices
• expect content to work flawlessly and look great across all devices
• HTML 5 custom design with coding as required
• must have good experiance in ecommerce website design
• eye catching, high quality look and feel and very user friedly ,very up-to date.
Nice to have
• picture slider show
• explain in writing what exactly i am getting in my ecommerce website
Should not have
• plain , basic design , old fashion looking ,cheap look

```html
<!DOCTYPE html>
<html lang="en">
<head>
<meta charset="utf-8">
<title>Plumbrook</title>
<link rel="stylesheet" href="https://fonts.googleapis.com/css2?family=Ubuntu:ital,wght@0,400;0,500;0,700;1,400&family=Arimo:wght@400;700&display=swap">
<style>
:root{
  --orange:#f78f20;
  --green:#9bcb3c;
  --green-dark:#86b62c;
  --bar:#2f2f2f;
  --bar-top:#3a3a3a;
  --ink:#555;
  --panel:#efefef;
  --line:#dcdcdc;
  --white:#fff;
}
*{box-sizing:border-box;margin:0;padding:0}
html,body{width:1200px;height:918px;overflow:hidden;background:var(--white)}
body{position:relative;font-family:"Ubuntu",sans-serif;color:var(--ink)}
.abs{position:absolute}

/* header */
.header{left:0;top:0;width:1200px;height:99px;background:var(--bar)}
.header-strip{left:0;top:0;width:1200px;height:31px;background:var(--bar-top);border-bottom:1px solid #262626}
.welcome{left:340px;top:8px;font-size:11px;font-style:italic;color:#ddd}
.account-links{right:110px;top:8px;display:flex;gap:22px;font-size:11px;color:#ccc}
.account-links span{display:flex;align-items:center;gap:5px}
.account-links .login{color:var(--green)}
.brand-name{left:130px;top:53px;display:flex;align-items:center;gap:9px;font-size:20px;font-weight:500;color:var(--white)}
.brand-name i{display:block;width:14px;height:14px;background:var(--green)}
.hotline{left:324px;top:46px;color:var(--white)}
.hotline-title{display:flex;align-items:center;gap:6px;font-size:14px;font-weight:500}
.badge{display:inline-flex;align-items:center;justify-content:center;width:20px;height:17px;background:var(--green);color:var(--bar);font-size:10px;font-weight:700;border-radius:2px}
.hotline-nums{margin-top:3px;padding-left:28px;font-size:15px;font-weight:500;color:var(--green)}
.search{left:616px;top:51px;display:flex;height:29px}
.search-input{width:234px;background:var(--white);font-size:10px;font-style:italic;color:#aaa;padding:9px 10px}
.search-btn{width:86px;background:var(--orange);color:var(--white);font-size:12px;font-weight:500;display:flex;align-items:center;justify-content:center}
.cart{left:955px;top:51px;height:29px;display:flex}
.cart-main{width:118px;background:var(--green);color:var(--white);font-size:12px;font-weight:500;display:flex;align-items:center;gap:6px;padding-left:8px}
.cart-main small{font-size:10px;font-weight:400}
.cart-cur{width:17px;background:var(--orange);color:var(--white);font-size:12px;font-weight:700;display:flex;align-items:center;justify-content:center}

/* nav */
.nav{left:0;top:99px;width:1200px;height:50px;background:var(--green);border-bottom:3px solid var(--green-dark)}
.nav a{position:absolute;top:0;height:47px;line-height:47px;color:var(--white);font-size:16px;font-weight:500;text-decoration:none}
.nav a.active{background:var(--green-dark);padding:0 13px}

/* categories */
.categories{left:97px;top:170px;width:231px;height:409px;background:var(--panel)}
.cat-head{height:39px;background:var(--orange);color:var(--white);font-size:14px;font-weight:500;display:flex;align-items:center;gap:8px;padding-left:13px}
.cat-list{list-style:none}
.cat-list li{height:34.6px;display:flex;align-items:center;justify-content:space-between;padding:0 8px 0 12px;font-family:"Arimo",sans-serif;font-size:11.5px;color:#666;border-bottom:1px solid var(--line)}
.cat-list li.current{color:var(--orange);font-weight:700}
.chev{width:15px;height:15px;border:1px solid #c8c8c8;border-radius:50%;display:flex;align-items:center;justify-content:center}

/* slider */
.slider{left:337px;top:168px;width:756px;height:302px;border:1px solid #d5d5d5;background:var(--white);padding:7px}
.slide-photo{width:100%;height:100%;background:radial-gradient(circle at 40% 40%,#a59a8a,#6c6458 60%,#3e3a35);position:relative}
.slide-caption{left:0;top:17px;background:rgba(30,30,30,.78);color:var(--white);font-size:15px;font-weight:500;padding:7px 14px}
.slide-arrow{top:130px}
.slide-dots{right:0;bottom:0;background:#222;padding:6px 8px;display:flex;gap:4px}
.slide-dots i{width:7px;height:7px;border-radius:50%;background:#888}
.slide-dots i.on{background:#eee}

/* promo banner */
.promo{left:337px;top:478px;width:756px;height:101px;background:linear-gradient(90deg,#2c3a1c,#46602a 45%,#6f9a35)}
.promo-title{left:40px;top:22px;color:var(--white);font-size:24px;font-weight:500;letter-spacing:.3px}
.promo-sub{left:40px;top:56px;color:#e6e6e6;font-size:14px}
.promo-grid{right:0;top:0;width:270px;height:101px;background:linear-gradient(120deg,rgba(60,160,60,0),#3fa33a 45%,#2d8a2b)}
.shop-now{left:573px;top:37px;width:96px;height:32px;background:var(--orange);color:var(--white);font-size:12px;font-weight:500;display:flex;align-items:center;justify-content:center;border-radius:2px}

/* news */
.news{left:97px;top:601px;width:231px;height:317px;background:var(--panel)}
.panel-head{height:42px;display:flex;align-items:center;justify-content:space-between;padding:0 4px 0 12px;font-size:14px;font-weight:500;color:#444;border-bottom:1px solid var(--line)}
.panel-head b{color:var(--orange);font-weight:500}
.pager{display:flex;gap:3px}
.pager i{width:16px;height:16px;border:1px solid #999;border-radius:50%;display:flex;align-items:center;justify-content:center;font-style:normal}
.pager i.off{border-color:#ccc}
.news-photo{margin:12px 8px 0;height:110px;border:1px solid #ccc;background:linear-gradient(#c9dceb,#8c9aa6 55%,#6a7f4b)}

/* products */
.products{left:337px;top:601px;width:764px;height:317px;background:var(--panel)}
.products .panel-head{padding-left:14px;padding-right:16px}
.product{top:84px}
</style>
</head>
<body>

<header class="abs header">
  <div class="abs header-strip"></div>
  <div class="abs welcome">Welcome Message for site visiter....</div>
  <nav class="abs account-links">
    <span><svg width="9" height="10" viewBox="0 0 9 10"><circle cx="4.5" cy="3" r="2.5" fill="#bbb"/><path d="M0 10c0-3 2-4.5 4.5-4.5S9 7 9 10z" fill="#bbb"/></svg>My Account</span>
    <span><svg width="10" height="9" viewBox="0 0 10 9"><path d="M1 5l3 3 5-7" stroke="#bbb" stroke-width="2" fill="none"/></svg>Checkout</span>
    <span class="login"><svg width="8" height="10" viewBox="0 0 8 10"><rect x="0" y="4" width="8" height="6" fill="#9bcb3c"/><path d="M2 4V2.5a2 2 0 014 0V4" stroke="#9bcb3c" stroke-width="1.4" fill="none"/></svg>Log In</span>
  </nav>

  <div class="abs brand-name"><i></i>Plumbrook</div>

  <div class="abs hotline">
    <div class="hotline-title"><span class="badge">24</span>hour messaging service on :</div>
    <div class="hotline-nums">0161-555-0142 &bull; 0800-555-0199</div>
  </div>

  <div class="abs search">
    <div class="search-input">Search here...</div>
    <div class="search-btn">SEARCH</div>
  </div>

  <div class="abs cart">
    <div class="cart-main">
      <svg width="16" height="13" viewBox="0 0 16 13"><path d="M0 1h3l2 8h9l2-6H4" stroke="#fff" stroke-width="1.6" fill="none"/><circle cx="6" cy="11.5" r="1.3" fill="#fff"/><circle cx="13" cy="11.5" r="1.3" fill="#fff"/></svg>
      CART <small>2 items</small>
    </div>
    <div class="cart-cur">£</div>
  </div>
</header>

<nav class="abs nav">
  <a style="left:327px">SHOP</a>
  <a class="active" style="left:393px">ABOUT US</a>
  <a style="left:521px">GROUND SOLUTIONS</a>
  <a style="left:709px">PLUMBROOK</a>
  <a style="left:841px">CONTACT US</a>
</nav>

<aside class="abs categories">
  <div class="cat-head">
    <svg width="13" height="10" viewBox="0 0 13 10"><rect width="13" height="2" fill="#fff"/><rect y="4" width="13" height="2" fill="#fff"/><rect y="8" width="13" height="2" fill="#fff"/></svg>
    CATEGORIES
  </div>
  <ul class="cat-list">
    <li>Lorem ipsum dolor<span class="chev"><svg width="5" height="7" viewBox="0 0 5 7"><path d="M1 0.5l3 3-3 3" stroke="#999" fill="none"/></svg></span></li>
    <li class="current">Sit amet consectetuer<span class="chev"><svg width="5" height="7" viewBox="0 0 5 7"><path d="M1 0.5l3 3-3 3" stroke="#999" fill="none"/></svg></span></li>
    <li>Adipiscing elit sed<span class="chev"><svg width="5" height="7" viewBox="0 0 5 7"><path d="M1 0.5l3 3-3 3" stroke="#999" fill="none"/></svg></span></li>
    <li>Diam nonummy nibh euismod<span class="chev"><svg width="5" height="7" viewBox="0 0 5 7"><path d="M1 0.5l3 3-3 3" stroke="#999" fill="none"/></svg></span></li>
    <li>Tincidunt ut laoreet dolore<span class="chev"><svg width="5" height="7" viewBox="0 0 5 7"><path d="M1 0.5l3 3-3 3" stroke="#999" fill="none"/></svg></span></li>
    <li>Magna aliquam erat volutpat<span class="chev"><svg width="5" height="7" viewBox="0 0 5 7"><path d="M1 0.5l3 3-3 3" stroke="#999" fill="none"/></svg></span></li>
    <li>Ut wisi enim ad minim veniam<span class="chev"><svg width="5" height="7" viewBox="0 0 5 7"><path d="M1 0.5l3 3-3 3" stroke="#999" fill="none"/></svg></span></li>
    <li>Lorem ipsum dolor<span class="chev"><svg width="5" height="7" viewBox="0 0 5 7"><path d="M1 0.5l3 3-3 3" stroke="#999" fill="none"/></svg></span></li>
    <li>Sit amet consectetuer<span class="chev"><svg width="5" height="7" viewBox="0 0 5 7"><path d="M1 0.5l3 3-3 3" stroke="#999" fill="none"/></svg></span></li>
    <li>Adipiscing elit sed<span class="chev"><svg width="5" height="7" viewBox="0 0 5 7"><path d="M1 0.5l3 3-3 3" stroke="#999" fill="none"/></svg></span></li>
  </ul>
</aside>

<section class="abs slider">
  <div class="slide-photo" role="img" aria-label="Photo of pebbles filling a black plastic gravel grid on a pathway">
    <div class="abs slide-caption">STONEGRID SYSTEM FOR PATHWAYS</div>
    <svg class="abs slide-arrow" style="left:20px" width="12" height="20" viewBox="0 0 12 20"><path d="M10 2L2 10l8 8" stroke="#fff" stroke-width="2.5" fill="none"/></svg>
    <svg class="abs slide-arrow" style="right:20px" width="12" height="20" viewBox="0 0 12 20"><path d="M2 2l8 8-8 8" stroke="#fff" stroke-width="2.5" fill="none"/></svg>
    <div class="abs slide-dots"><i></i><i class="on"></i><i></i><i></i></div>
  </div>
</section>

<section class="abs promo" role="img" aria-label="Banner photo of grass lawn with green hexagonal paving grid">
  <div class="abs promo-grid"></div>
  <div class="abs promo-title">STABILISED GRAVEL PAVING GRIDS</div>
  <div class="abs promo-sub">Magna aliquam erat volutpat</div>
  <div class="abs shop-now">SHOP NOW</div>
</section>

<section class="abs news">
  <div class="panel-head">
    <span>LATEST <b>NEWS</b></span>
    <span class="pager">
      <i class="off"><svg width="5" height="7" viewBox="0 0 5 7"><path d="M4 0.5l-3 3 3 3" stroke="#bbb" fill="none"/></svg></i>
      <i><svg width="5" height="7" viewBox="0 0 5 7"><path d="M1 0.5l3 3-3 3" stroke="#555" fill="none"/></svg></i>
    </span>
  </div>
  <div class="news-photo" role="img" aria-label="Photo of a house with a gravel driveway"></div>
</section>

<section class="abs products">
  <div class="panel-head">
    <span>NEW <b>PRODUCTS</b></span>
    <span class="pager">
      <i class="off"><svg width="5" height="7" viewBox="0 0 5 7"><path d="M4 0.5l-3 3 3 3" stroke="#bbb" fill="none"/></svg></i>
      <i><svg width="5" height="7" viewBox="0 0 5 7"><path d="M1 0.5l3 3-3 3" stroke="#555" fill="none"/></svg></i>
    </span>
  </div>
  <svg class="abs product" style="left:87px" width="100" height="110" viewBox="0 0 100 110" role="img" aria-label="Product photo of a gravel grid panel"><path d="M50 3L96 29V81L50 107L4 81V29Z" fill="#8e8a82" stroke="#f78f20" stroke-width="5"/></svg>
  <svg class="abs product" style="left:329px" width="100" height="110" viewBox="0 0 100 110" role="img" aria-label="Product photo of a grass reinforcement grid"><path d="M50 3L96 29V81L50 107L4 81V29Z" fill="#7d9a56" stroke="#9bcb3c" stroke-width="5"/></svg>
  <svg class="abs product" style="left:570px" width="100" height="110" viewBox="0 0 100 110" role="img" aria-label="Product photo of a driveway paving grid"><path d="M50 3L96 29V81L50 107L4 81V29Z" fill="#8e8a82" stroke="#f78f20" stroke-width="5"/></svg>
</section>

</body>
</html>
```